Corporate A4 Advert for Worldwide Timber Trader/Agent

We need a new professional company ad, which will be used in worldwide magazine publications. something sophisticated.
Our website - www.brantelsupply.co.uk - for info. We are timber agents and sell timber from one part of the world to another.
I will upload a selection of product photos to include - suggest using not all but a selection of some them, to showcase the product. Our buyers purchase both logs and sawn timber
We would like this ad to list our source areas and product groups.
Our company colour is British Racing Green
Updates

Need extra days to review

Target Market(s)

timber buyers

Industry/Entity Type

Timber

Colors
00AB8E
00BBA5
67D7C9
C6EFE9
E9F9F6

Requirements
Must have
• company logo

```html
<!DOCTYPE html>
<html lang="en">
<head>
<meta charset="utf-8">
<title>Brantel Supply — Timber Advert</title>
<link rel="stylesheet" href="https://fonts.googleapis.com/css2?family=Jost:wght@400;500;600;700&display=swap">
<style>
  :root {
    --racing-green: #0d4a2b;
    --paper: #f1f1f0;
    --ink: #1c1c1c;
    --mark-faint: #d8dcdb;
    --wood-light: #d08a52;
    --wood-mid: #a45a2c;
    --wood-dark: #6b3a1c;
    --soil: #9a4b2a;
    --sky: #b9c3c8;
    --forest: #3c5a34;
    --stage: #ffffff;
  }
  * { box-sizing: border-box; margin: 0; padding: 0; }
  html, body { width: 1076px; height: 1200px; overflow: hidden; background: var(--stage); }
  body { font-family: "Jost", sans-serif; color: var(--ink); }

  .advert {
    position: relative;
    width: 1076px;
    height: 1200px;
    background: var(--paper);
    overflow: hidden;
  }

  /* Header */
  .header { position: absolute; left: 0; top: 0; width: 1076px; height: 330px; display: flex; }
  .brand-block {
    width: 420px; height: 330px; background: var(--paper);
    display: flex; align-items: center; justify-content: center; gap: 16px;
  }
  .brand-dot { width: 34px; height: 34px; border-radius: 50%; background: var(--racing-green); }
  .brand-name { font-weight: 600; font-size: 62px; color: var(--racing-green); letter-spacing: 0.5px; }
  .hero-photo {
    flex: 1; height: 330px;
    background: linear-gradient(160deg, var(--sky) 0%, var(--wood-light) 22%, var(--wood-mid) 60%, var(--soil) 100%);
  }

  /* Headline band */
  .headline-band {
    position: absolute; left: 0; top: 330px; width: 1076px; height: 195px;
    background: var(--racing-green); color: #fff; text-align: center;
    padding: 24px 50px 0;
  }
  .headline { font-weight: 600; font-size: 35px; line-height: 44px; letter-spacing: 0.3px; text-transform: uppercase; }
  .tagline { font-size: 17.5px; line-height: 25px; margin-top: 20px; font-weight: 400; }

  /* Faint decoration */
  .decor-circle {
    position: absolute; left: 790px; top: 560px; width: 460px; height: 460px;
    border-radius: 50%; background: var(--mark-faint); opacity: 0.55;
  }

  .intro {
    position: absolute; left: 55px; top: 548px; width: 760px;
    font-size: 16.5px; line-height: 24.5px;
  }

  /* Photo collage */
  .collage { position: absolute; left: 0; top: 690px; width: 760px; height: 165px; }
  .collage-photo { position: absolute; box-shadow: 0 4px 10px rgba(0,0,0,0.35); }
  .collage-photo.sawn { left: 45px; top: 10px; width: 190px; height: 150px;
    background: linear-gradient(180deg, var(--wood-mid), var(--wood-dark) 80%, var(--soil)); }
  .collage-photo.truck { left: 225px; top: 0; width: 280px; height: 165px; z-index: 2;
    background: linear-gradient(180deg, var(--forest) 0%, var(--wood-light) 45%, #e8e8e8 62%, var(--soil) 100%); }
  .collage-photo.logs { left: 500px; top: 14px; width: 170px; height: 135px;
    background: linear-gradient(170deg, var(--sky), var(--wood-light) 40%, var(--wood-mid)); }

  /* Service section */
  .service { position: absolute; left: 55px; top: 870px; width: 690px; }
  .service-title { font-weight: 600; font-size: 23px; color: var(--racing-green); margin-bottom: 6px; }
  .service-copy { font-size: 15.5px; line-height: 21px; text-align: justify; }

  /* Footer */
  .yard-photo {
    position: absolute; left: 0; top: 1040px; width: 1076px; height: 105px;
    background: linear-gradient(180deg, var(--sky) 0%, var(--forest) 30%, var(--wood-mid) 60%, var(--soil) 100%);
  }
  .footer {
    position: absolute; left: 0; top: 1145px; width: 1076px; height: 55px;
    background: var(--racing-green); color: #fff;
    display: flex; align-items: center; justify-content: center;
  }
  .website { font-size: 22px; letter-spacing: 3px; }
</style>
</head>
<body>
  <main class="advert">
    <header class="header">
      <div class="brand-block">
        <span class="brand-dot"></span>
        <span class="brand-name">Brantel</span>
      </div>
      <div class="hero-photo" role="img" aria-label="Stacked tropical hardwood logs on red earth"></div>
    </header>

    <section class="headline-band">
      <h1 class="headline">The Natural Source of World Hardwoods<br>&amp; Clear Softwoodsy</h1>
      <p class="tagline">We take pride in trading timber globally and responsibly. Developing and nurturing clients<br>and suppliers is critical to our success.</p>
    </section>

    <div class="decor-circle" aria-hidden="true"></div>

    <p class="intro">Founded in 1981, Brantel Supply Ltd is a UK-based family business with deep roots in the international timber trade.<br>We specialise in sourcing Tropical and Temperate Hardwoods as well as Softwood Clears, offering bespoke solutions tailored to the unique needs of both buyers and suppliers. Our goal is always to build long-term relationships through trust, transparency, and practical business support.</p>

    <div class="collage">
      <div class="collage-photo sawn" role="img" aria-label="Bundled sawn hardwood timber"></div>
      <div class="collage-photo truck" role="img" aria-label="Logging truck carrying a large log"></div>
      <div class="collage-photo logs" role="img" aria-label="Cut log ends in a forest yard"></div>
    </div>

    <section class="service">
      <h2 class="service-title">Service to our Buyers</h2>
      <p class="service-copy">Brantel Supply, our traders are responsible for both selling and procuring their products. They travel extensively, regularly visiting both their clients and suppliers, and in so doing are always in possession of crucial market, product, and shipping knowledge that is relevant and up to date. The traders are supported by their own trader’s assistant, and our finance and logistics department is responsible for ensuring accurate and timely documentation to support your orders and shipments.</p>
    </section>

    <div class="yard-photo" role="img" aria-label="Log yard with rows of hardwood logs beside the forest"></div>

    <footer class="footer">
      <span class="website">www.brantelsupply.co.uk</span>
    </footer>
  </main>
</body>
</html>
```